Business Card Design Project and Logo Enhancement

This project requires designing a business card for a construction company. It also requires small enhancements on provided logo.
Summary about the company:
Name: Korvellan Group.
Future website. www.korvellan.ca
Korvellan is a home redesign and renovation company providing services in Ottawa Canada area.
It offers the following services:
- Home Additions
- Roofing
- Eavestroughing & Soffit Fascia
- Fencing
- Decks
- Window Installation, and
- Indoor Renovation Including ( Kitchen redesign, Basement finishing, bathroom upgrades, etc)
Logo and Company name background:
Korvellan refers to an ancient empire that was located in Balkans called Veltarians.
Provided logo represents the symbol of Veltarians.
Project Expectation:
Logo:
Attached logo is too SIMPLe. It would be nice adding a bit of design.
That could include different colors or adding a bit of style to the logo.
Business Card
Initial preferred layout/content ( open to other suggestions) :
Preferred type: Vertical with rounded corners
Front side should have:
- Logo
- Company Name
- First Name/ Last name: Ie: Edmir Kollqaj
- Office Phone:
- Direct Phone:
- QR Code linking to www.korvellan.ca, and
- website url. www. korvellan.ca
Back end shall contain:
Professional services offered:
- Large company logo covering most of the card as a water mark
- Divisions Services offered
- Roofing
- Eavestroughing, Soffit, Fascia
- Fencing and Decks
- Indoor Design and Renovation
- Company Phone and
- Company website address: www.korvellan.ca
PSD and other raw files must be provided by the winner.

```html
<!DOCTYPE html>
<html lang="en">
<head>
<meta charset="UTF-8">
<title>Korvellan Group — Business Card</title>
<link href="https://fonts.googleapis.com/css2?family=Cinzel:wght@400&family=Jost:wght@500&family=Open+Sans:wght@400&display=swap" rel="stylesheet">
<style>
  :root {
    --page-bg: #ffffff;
    --card-bg: #000000;
    --gold: #c9a23a;
    --ink: #ffffff;
  }
  html, body {
    margin: 0;
    padding: 0;
    width: 1200px;
    height: 900px;
    overflow: hidden;
    background: var(--page-bg);
  }
  .canvas {
    position: relative;
    width: 1200px;
    height: 900px;
  }
  .card {
    position: absolute;
    left: 347px;
    top: 58px;
    width: 506px;
    height: 784px;
    background: var(--card-bg);
    border-radius: 42px;
    overflow: hidden;
  }
  .brand-ring {
    position: absolute;
    left: 150px;
    top: 51px;
    width: 192px;
    height: 192px;
  }
  .brand-name {
    position: absolute;
    left: 0;
    right: 0;
    top: 278px;
    margin: 0;
    text-align: center;
    padding-left: 44px;
    font-family: "Cinzel", serif;
    font-weight: 400;
    font-size: 44px;
    letter-spacing: 1px;
    color: var(--gold);
  }
  .person-name {
    position: absolute;
    left: 131px;
    top: 425px;
    margin: 0;
    font-family: "Jost", sans-serif;
    font-weight: 500;
    font-size: 30px;
    color: var(--ink);
  }
  .contact-list {
    position: absolute;
    left: 59px;
    top: 562px;
    margin: 0;
    padding: 0;
    list-style: none;
    font-family: "Open Sans", sans-serif;
    font-size: 22px;
    color: var(--ink);
  }
  .contact-list li {
    height: 48px;
    line-height: 32px;
    white-space: pre;
  }
  .contact-label {
    display: inline-block;
  }
  .contact-label.fixed {
    width: 148px;
  }
</style>
</head>
<body>
<div class="canvas">
  <section class="card">
    <svg class="brand-ring" viewBox="0 0 192 192" aria-hidden="true">
      <circle cx="96" cy="96" r="93" fill="none" stroke="#c9a23a" stroke-width="4"/>
    </svg>
    <h1 class="brand-name">Korvellan Group</h1>
    <p class="person-name">Edmir KOLLQAJ</p>
    <ul class="contact-list">
      <li><span class="contact-label">office phone:</span>  000 000 000 00</li>
      <li><span class="contact-label">direct phone:</span>  000 000 000 00</li>
      <li><span class="contact-label fixed">QR code</span>:  0000000</li>
      <li><span class="contact-label fixed">web</span>:  www. korvellan.ca</li>
    </ul>
  </section>
</div>
</body>
</html>
```